Corwen Physical Therapy Website

I would need a clean modern website built to showcase my Physical therapy brand and services. I would need a simple but descriptive website that can ultimately connect my patients to my electronic medical portal so they may book an appointment..

```html
<!DOCTYPE html>
<html lang="en">
<head>
<meta charset="utf-8">
<title>Corwen Physical Therapy &amp; Wellness</title>
<link rel="stylesheet" href="https://fonts.googleapis.com/css2?family=Poppins:wght@300;400;500;600;700&family=Montserrat:ital,wght@0,400;0,500;0,600;0,700;1,400&display=swap">
<style>
:root{
  --green:#86c440;
  --green-dark:#2f9a4c;
  --teal:#16897d;
  --teal-dark:#0f6f65;
  --blue:#5b6cbc;
  --ink:#2f3337;
  --muted:#6d7278;
  --mist:#eef4f3;
  --white:#ffffff;
}
*{box-sizing:border-box;margin:0;padding:0}
html,body{width:1200px;height:4313px;overflow:hidden}
body{font-family:"Montserrat",sans-serif;color:var(--ink);background:var(--white)}
.page{position:relative;width:1200px;height:4313px;overflow:hidden}
.abs{position:absolute}
.photo{position:absolute}

/* header */
.topbar{left:636px;top:0;width:564px;height:33px;background:var(--teal);clip-path:polygon(22px 0,100% 0,100% 100%,0 100%);color:#fff;font-size:11.5px;display:flex;align-items:center;gap:28px;padding-left:40px}
.topbar span{display:flex;align-items:center;gap:8px}
.topbar i{display:inline-block;width:20px;height:20px;border-radius:50%;background:var(--green);position:relative}
.brand{left:110px;top:28px;display:flex;align-items:center;gap:10px}
.brand .mark{width:50px;height:50px;border-radius:50%;background:var(--teal)}
.brand .name{font-family:"Poppins",sans-serif;font-weight:700;font-size:34px;color:var(--teal);letter-spacing:1px}
.nav{top:66px;left:0;font-family:"Poppins",sans-serif;font-size:12.5px;font-weight:500;color:var(--ink)}
.nav a{position:absolute;white-space:nowrap;text-decoration:none;color:inherit}
.nav a.active{color:var(--green)}
.nav a.active::after{content:"";position:absolute;left:0;right:0;top:26px;height:3px;background:var(--green)}

/* hero */
.hero-photo{left:0;top:109px;width:1200px;height:611px;background:linear-gradient(90deg,#f1f2f1 0%,#ececea 45%,#d9d6cf 70%,#cfd6de 100%)}
.hero-kicker{left:115px;top:276px;font-family:"Poppins",sans-serif;font-size:20px;letter-spacing:3px;color:var(--ink)}
.hero-title{left:109px;top:303px;font-family:"Poppins",sans-serif;font-weight:700;font-size:50px;color:var(--green-dark);letter-spacing:1px}
.hero-sub{left:109px;top:366px;font-family:"Poppins",sans-serif;font-weight:400;font-size:36px;color:var(--green);letter-spacing:1px}
.btn-fill{background:var(--green);color:#fff;border-radius:30px;font-family:"Poppins",sans-serif;font-weight:600;font-size:13.5px;letter-spacing:1px;display:flex;align-items:center;justify-content:center;gap:6px}
.btn-line{border:2px solid var(--teal);color:var(--teal);border-radius:30px;font-family:"Poppins",sans-serif;font-weight:600;font-size:13.5px;letter-spacing:1px;display:flex;align-items:center;justify-content:center}
.slide-arrow{top:306px;width:30px;height:44px}

/* section headings */
.kicker{font-family:"Poppins",sans-serif;font-size:14.5px;letter-spacing:3px;color:var(--green)}
.heading{font-family:"Poppins",sans-serif;font-weight:400;font-size:42px;color:var(--ink);white-space:nowrap}
.heading b{font-weight:700;color:var(--teal)}
.rule{height:3px;width:42px;background:var(--green)}
.copy{font-size:13px;line-height:27px;color:var(--muted)}

/* about */
.orbit-label{font-family:"Poppins",sans-serif;font-weight:600;font-size:10.5px;line-height:14px;color:var(--teal);text-align:center}

/* services */
.services{left:0;top:1281px;width:1200px;height:554px;background:linear-gradient(180deg,#5667b8 0%,#6172c0 60%,#5a6bb9 100%)}
.services .kicker{color:#e8ebfa}
.services .heading{color:#fff}
.services .heading b{color:#fff}
.svc{top:1448px;width:226px;height:290px;background:#fff;box-shadow:0 4px 14px rgba(0,0,0,.12)}
.svc .img{position:absolute;left:6px;top:6px;width:214px;height:182px}
.svc .icon{position:absolute;left:83px;top:159px;width:60px;height:60px;border-radius:50%;background:var(--teal);border:4px solid #fff}
.svc h3{position:absolute;left:0;right:0;top:228px;text-align:center;font-family:"Poppins",sans-serif;font-weight:600;font-size:16px;color:var(--ink)}
.svc p{position:absolute;left:0;right:0;top:255px;text-align:center;font-size:11px;color:var(--muted)}

/* portal */
.portal-green{left:733px;top:1835px;width:467px;height:527px;background:var(--green)}
.laptop-body{left:603px;top:1928px;width:452px;height:300px;background:#222;border-radius:10px 10px 0 0}
.laptop-base{left:546px;top:2222px;width:562px;height:14px;background:linear-gradient(#9a9c9e,#5d5f61);border-radius:0 0 16px 16px}

/* testimonials */
.reviews{left:0;top:2364px;width:1200px;height:475px;background:var(--mist)}
.quote{top:2531px;width:429px;height:233px;background:#fff}
.quote p{position:absolute;left:33px;top:34px;width:370px;font-style:italic;font-size:13.2px;line-height:27px;color:var(--muted)}
.quote .avatar{position:absolute;left:36px;top:165px;width:44px;height:44px;border-radius:50%;background:linear-gradient(135deg,#d8c3b1,#a99585)}
.quote .who{position:absolute;left:92px;top:166px;font-family:"Poppins",sans-serif;font-size:13.5px;font-weight:500;color:var(--teal)}
.quote .stars{position:absolute;left:90px;top:184px;color:#f5b400;font-size:19px;letter-spacing:1px}

/* blogs */
.post{top:2988px;width:303px;height:300px;background:#fff;border:1px solid #dfe3e3}
.post .img{position:absolute;left:0;top:0;width:301px;height:187px}
.post .date{position:absolute;left:0;top:166px;height:21px;padding:0 14px;background:var(--green);color:#fff;font-family:"Poppins",sans-serif;font-weight:600;font-size:10.5px;line-height:21px}
.post h4{position:absolute;left:23px;top:210px;width:260px;font-family:"Poppins",sans-serif;font-weight:600;font-size:13.5px;line-height:19px;color:var(--ink)}
.post a{position:absolute;left:23px;top:262px;font-family:"Poppins",sans-serif;font-weight:600;font-size:10.5px;color:var(--teal);text-decoration:none}

/* booking */
.field{left:119px;width:423px;border:1px solid #c9cfcf;background:#fff;font-size:11px;font-weight:600;color:var(--ink);padding:15px 0 0 22px}

/* footer */
.footer{left:0;top:3925px;width:1200px;height:320px;background:var(--teal)}
.footbar{left:0;top:4245px;width:1200px;height:68px;background:var(--teal-dark);color:#cfe6e2;font-size:10.5px;text-align:center;line-height:68px}
.fcol h5{font-family:"Poppins",sans-serif;font-weight:600;font-size:14px;color:#fff}
.fcol h5::after{content:"";display:block;width:34px;height:3px;background:var(--green);margin-top:9px}
.fcol ul{list-style:none;margin-top:16px}
.fcol li{font-size:12px;color:#e6f3f1;height:27.5px}
.contact li{display:flex;gap:10px;align-items:flex-start;height:23px}
.social{top:4152px;left:823px;display:flex;gap:7px}
.social span{width:30px;height:30px;border-radius:50%;background:#fff;display:block}
</style>
</head>
<body>
<div class="page">

  <!-- header -->
  <div class="abs topbar">
    <span><i></i>CALL US TODAY (555) 014 2286</span>
    <span><i></i>hello@corwentherapy.com</span>
  </div>
  <div class="abs brand"><span class="mark"></span><span class="name">CORWEN</span></div>
  <nav class="abs nav">
    <a class="active" style="left:372px">HOME</a>
    <a style="left:462px">ABOUT US</a>
    <a style="left:573px">OUR SERVICES</a>
    <a style="left:713px">WHY CHOOSE US</a>
    <a style="left:869px">TESTIMONIALS</a>
    <a style="left:1008px">CONTACT US</a>
  </nav>

  <!-- hero -->
  <div class="photo hero-photo" role="img" aria-label="Physical therapist stretching a smiling patient's arm in a bright clinic"></div>
  <svg class="abs" style="left:0;top:620px" width="1200" height="110" viewBox="0 0 1200 110">
    <path d="M0 90 C250 30 520 30 760 60 C930 82 1080 60 1200 40 L1200 110 L0 110 Z" fill="#fff"/>
    <path d="M80 70 C300 32 560 40 760 62 C930 80 1080 58 1200 40" fill="none" stroke="#86c440" stroke-width="6"/>
  </svg>
  <svg class="abs slide-arrow" style="left:24px" viewBox="0 0 30 44"><path d="M20 6 L6 22 L20 38" fill="none" stroke="#8f99a0" stroke-width="4"/></svg>
  <svg class="abs slide-arrow" style="left:1153px" viewBox="0 0 30 44"><path d="M10 6 L24 22 L10 38" fill="none" stroke="#8f99a0" stroke-width="4"/></svg>
  <div class="abs hero-kicker">WELCOME TO OUR WEBSITE</div>
  <div class="abs hero-title">CORWEN PHYSICAL</div>
  <div class="abs hero-sub">THERAPY &amp; WELLNESS</div>
  <div class="abs btn-fill" style="left:109px;top:432px;width:244px;height:48px">BOOK APPOINTMENT
    <svg width="18" height="10" viewBox="0 0 18 10"><path d="M0 5 H16 M12 1 L16 5 L12 9" fill="none" stroke="#fff" stroke-width="1.6"/></svg>
  </div>

  <!-- about -->
  <svg class="abs" style="left:120px;top:790px" width="450" height="420" viewBox="0 0 450 420">
    <circle cx="223" cy="214" r="209" fill="none" stroke="#16897d" stroke-width="2.5" stroke-dasharray="1100 220" transform="rotate(120 223 214)"/>
    <circle cx="223" cy="5" r="5" fill="#86c440"/>
    <circle cx="37" cy="120" r="5" fill="#86c440"/>
    <circle cx="392" cy="124" r="5" fill="#86c440"/>
    <path d="M90 380 C160 350 230 410 330 375" fill="none" stroke="#86c440" stroke-width="5"/>
    <path d="M100 395 C170 368 240 425 340 390" fill="none" stroke="#16897d" stroke-width="4"/>
  </svg>
  <div class="photo" style="left:146px;top:818px;width:394px;height:394px;border-radius:50%;background:radial-gradient(circle at 45% 40%,#f4f1ec 0%,#ddd3c6 55%,#c7a98e 100%)" role="img" aria-label="Therapist stretching a patient's leg on a treatment mat"></div>
  <div class="abs orbit-label" style="left:283px;top:774px;width:120px">SPORTS INJURY<br>RECOVERY</div>
  <div class="abs orbit-label" style="left:85px;top:891px;width:88px">PHYSICAL<br>THERAPY</div>
  <div class="abs orbit-label" style="left:520px;top:893px;width:76px;text-align:left">BODY<br>WELLNESS</div>

  <div class="abs kicker" style="left:633px;top:826px">OUR THERAPY CENTER</div>
  <div class="abs heading" style="left:633px;top:846px">ABOUT <b>CORWEN</b></div>
  <div class="abs rule" style="left:633px;top:902px"></div>
  <p class="abs copy" style="left:634px;top:918px;width:450px">Lorem Ipsum is simply dummy text of the printing and typesetting industry. Lorem Ipsum has been the industry's standard dummy text ever since the 1500s, when an unknown printer took a galley of type and scrambled it to make a type specimen book.</p>
  <p class="abs copy" style="left:634px;top:1041px;width:450px">Lorem Ipsum is simply dummy text of the printing and typesetting industry. Lorem Ipsum has been the industry's standard dummy text.</p>
  <div class="abs btn-line" style="left:633px;top:1125px;width:168px;height:47px">LEARN MORE</div>

  <!-- services -->
  <div class="abs services" role="img" aria-label="Soft blue overlay over a therapist treating a patient's shoulder"></div>
  <div class="abs kicker" style="left:0;width:1200px;text-align:center;top:1328px">WHAT WE DO</div>
  <div class="abs heading" style="left:0;width:1200px;text-align:center;top:1346px">SERVICE <b>PROVIDE</b></div>
  <div class="abs rule" style="left:579px;top:1400px"></div>

  <div class="abs svc" style="left:126px">
    <div class="photo img" style="background:linear-gradient(135deg,#cfe0ea,#b7c0c4 55%,#8f979b)" role="img" aria-label="Therapist assisting a patient with a shoulder stretch"></div>
    <div class="icon"></div><h3>Injury Pain Relief</h3><p>Donec convallis pede venenatis</p>
  </div>
  <div class="abs svc" style="left:365px">
    <div class="photo img" style="background:linear-gradient(135deg,#eef1f1,#cdd8da 55%,#a9b8bb)" role="img" aria-label="Therapist working on a patient lying on a treatment table"></div>
    <div class="icon"></div><h3>Physical Therapy</h3><p>Donec convallis pede venenatis</p>
  </div>
  <div class="abs svc" style="left:599px">
    <div class="photo img" style="background:linear-gradient(135deg,#f0d8c6,#d9a98a 55%,#b98266)" role="img" aria-label="Hands giving a close-up massage"></div>
    <div class="icon"></div><h3>Wellness Service</h3><p>Donec convallis pede venenatis</p>
  </div>
  <div class="abs svc" style="left:832px">
    <div class="photo img" style="background:linear-gradient(135deg,#d9dde0,#bcb6b3 50%,#e77d62)" role="img" aria-label="Back with highlighted spine showing joint pain"></div>
    <div class="icon"></div><h3>Joint Pain Relief</h3><p>Donec convallis pede venenatis</p>
  </div>

  <!-- portal -->
  <div class="abs portal-green"></div>
  <div class="abs kicker" style="left:141px;top:1953px">BOOK YOUR APPOINTMENT</div>
  <div class="abs heading" style="left:140px;top:1974px">MEDICAL <b>PORTAL</b></div>
  <p class="abs copy" style="left:142px;top:2045px;width:400px">Lorem Ipsum is simply dummy text of the printing and typesetting industry. Lorem Ipsum has been the industry's standard dummy text ever since the 1500s, when an unknown printer took a galley of type and scrambled it to make a type specimen book.</p>
  <div class="abs btn-line" style="left:140px;top:2186px;width:169px;height:47px">BOOK NOW</div>
  <div class="abs laptop-body"></div>
  <div class="photo" style="left:612px;top:1937px;width:434px;height:285px;background:linear-gradient(180deg,#ffffff 0%,#f3f6f6 60%,#e3f1ef 100%);border-left:18px solid #2bb6a7" role="img" aria-label="Appointment booking timeline dashboard on the medical portal"></div>
  <div class="abs laptop-base"></div>

  <!-- testimonials -->
  <div class="abs reviews"></div>
  <div class="abs heading" style="left:0;width:1200px;text-align:center;top:2426px;font-size:35px">WHAT <b>PEOPLE SAYS</b></div>
  <div class="abs rule" style="left:584px;top:2479px;width:36px"></div>
  <div class="abs quote" style="left:161px">
    <p>Lorem ipsum dolor sit amet, consectetur adipiscing elit, sed do eiusmod tempor incididunt ut labore et dolore magna aliqua Ut enim ad minim veniam, quis nostrud exercitation ullamco laboris nisi ut al</p>
    <div class="avatar" role="img" aria-label="Client portrait"></div>
    <div class="who">Dana Holt</div><div class="stars">★★★★★</div>
  </div>
  <div class="abs quote" style="left:616px">
    <p>Lorem ipsum dolor sit amet, consectetur adipiscing elit, sed do eiusmod tempor incididunt ut labore et dolore magna aliqua Ut enim ad minim veniam, quis nostrud exercitation ullamco laboris nisi ut al</p>
    <div class="avatar" role="img" aria-label="Client portrait"></div>
    <div class="who">Mira Lenz</div><div class="stars">★★★★★</div>
  </div>

  <!-- blogs -->
  <div class="abs heading" style="left:125px;top:2905px;font-size:35px">RECENT <b>BLOGS</b></div>
  <div class="abs rule" style="left:126px;top:2957px"></div>
  <div class="abs post" style="left:126px">
    <div class="photo img" style="background:linear-gradient(135deg,#f1cdb6,#e8a58c 50%,#c98468)" role="img" aria-label="Therapist's hands on a back with highlighted spine"></div>
    <div class="date">28 MAY 2021</div>
    <h4>Lorem ipsum dolor sit amet, consectetur adipiscing elit sed do</h4><a>LEARN MORE →</a>
  </div>
  <div class="abs post" style="left:440px">
    <div class="photo img" style="background:linear-gradient(135deg,#e6e9ea,#aeb9b7 55%,#5f8f7e)" role="img" aria-label="Therapist guiding a patient's leg exercise"></div>
    <div class="date">28 MAY 2021</div>
    <h4>Lorem ipsum dolor sit amet, consectetur adipiscing elit sed do</h4><a>LEARN MORE →</a>
  </div>
  <div class="abs post" style="left:755px">
    <div class="photo img" style="background:linear-gradient(135deg,#6b4a32,#b88a64 50%,#e6c9a8)" role="img" aria-label="Relaxing head massage in a spa setting"></div>
    <div class="date">28 MAY 2021</div>
    <h4>Lorem ipsum dolor sit amet, consectetur adipiscing elit sed do</h4><a>LEARN MORE →</a>
  </div>

  <!-- booking -->
  <div class="photo" style="left:0;top:3386px;width:1200px;height:540px;background:linear-gradient(90deg,#f7f8f8 0%,#f3f4f4 50%,#dfe2e3 70%,#c9cdd0 100%)" role="img" aria-label="Therapist treating a senior patient's shoulder in a bright room"></div>
  <div class="abs heading" style="left:118px;top:3446px;font-size:33px">BOOK YOUR <b>APPOINTMENT</b></div>
  <div class="abs rule" style="left:119px;top:3491px;width:52px"></div>
  <div class="abs field" style="top:3524px;height:42px">Name*</div>
  <div class="abs field" style="top:3576px;height:42px">Email address*</div>
  <div class="abs field" style="top:3626px;height:42px">Phone*</div>
  <div class="abs field" style="top:3678px;height:80px">Message</div>
  <div class="abs btn-fill" style="left:119px;top:3775px;width:154px;height:39px;font-size:12.5px">SUBMIT NOW</div>

  <!-- footer -->
  <svg class="abs" style="left:0;top:3868px" width="1200" height="60" viewBox="0 0 1200 60">
    <path d="M0 50 C300 10 700 8 1200 16 L1200 60 L0 60 Z" fill="#16897d"/>
    <path d="M0 50 C300 10 700 8 1200 16" fill="none" stroke="#86c440" stroke-width="5"/>
  </svg>
  <div class="abs footer"></div>
  <div class="abs" style="left:146px;top:4040px;display:flex;flex-direction:column;align-items:center;gap:14px;width:160px">
    <span style="width:60px;height:60px;border-radius:50%;background:#fff;display:block"></span>
    <span style="font-family:'Poppins',sans-serif;font-weight:700;font-size:36px;color:#fff;letter-spacing:1px">CORWEN</span>
  </div>
  <div class="abs fcol" style="left:413px;top:3999px">
    <h5>QUICK LINKS</h5>
    <ul><li>Home</li><li>About Us</li><li>Our Services</li><li>New Products</li><li>Contact Us</li></ul>
  </div>
  <div class="abs fcol" style="left:609px;top:3999px">
    <h5>RESOURCES</h5>
    <ul><li>News</li><li>Testimonials</li><li>Privacy Policy</li><li>Terms &amp; Condition</li></ul>
  </div>
  <div class="abs fcol contact" style="left:827px;top:3999px">
    <h5>CONTACT US</h5>
    <ul>
      <li><svg width="12" height="15" viewBox="0 0 12 15"><path d="M6 0 C2.7 0 0 2.6 0 5.8 C0 10 6 15 6 15 C6 15 12 10 12 5.8 C12 2.6 9.3 0 6 0 Z" fill="#fff"/><circle cx="6" cy="5.8" r="2.2" fill="#16897d"/></svg>Office Halden | Brookside Lane 14</li>
      <li style="padding-left:22px">Office Merton | Elm Row 8</li>
      <li><svg width="12" height="12" viewBox="0 0 12 12"><path d="M2 0 L4.5 2.5 L3.2 4.2 C4 6 6 8 7.8 8.8 L9.5 7.5 L12 10 L10.5 12 C5 11.5 0.5 7 0 1.5 Z" fill="#fff"/></svg>Tel: (555) 017 4420</li>
      <li><svg width="13" height="10" viewBox="0 0 13 10"><rect width="13" height="10" fill="#fff"/><path d="M0 0 L6.5 5.5 L13 0" fill="none" stroke="#16897d" stroke-width="1.2"/></svg>Email: info@corwen.com</li>
    </ul>
  </div>
  <div class="abs social"><span></span><span></span><span></span><span></span></div>
  <div class="abs footbar">© 2021 Corwen | All Rights Reserved &nbsp;|&nbsp; Terms &amp; Condition</div>

</div>
</body>
</html>
```